Flyer-Design für Beratungsunternehmen
Vielen Dank für die professionelle und überdurchschnittliche Unterstützung
Zielgruppe
Supervision, Coaching, Beratung
Plus digitale Beratung via App, sonstiger moderner Medien
für Organisationen, Firmen, Institutionen, Privatpersonen
Aufgabenstellung
Kreatives Design, modern, hochwertig
symphatisch, vertrauensvoll, transparent, ansprechend
Texte, Inhalte und Bilder siehe download
Sehr wichtig corporate design laut homepage www.reflexionamufer.de

```html
<!DOCTYPE html>
<html lang="de">
<head>
<meta charset="utf-8">
<title>Reflexion am Ufer – Flyer Innenseite</title>
<link href="https://fonts.googleapis.com/css2?family=Didact+Gothic&family=Saira+Semi+Condensed:wght@400;700&display=swap" rel="stylesheet">
<style>
  :root {
    --orange: #f39200;
    --orange-light: #f7a823;
    --green: #8cbf26;
    --green-soft: #d3e6a8;
    --text: #555555;
    --paper: #f4f4f4;
    --white: #ffffff;
    --ring: #e2e2e2;
  }
  html, body { margin: 0; padding: 0; overflow: hidden; }
  body { width: 1200px; height: 600px; background: var(--paper); }
  .flyer {
    position: relative; width: 1200px; height: 600px; overflow: hidden;
    background: var(--paper); color: var(--text);
    font-family: "Didact Gothic", "Century Gothic", sans-serif;
  }
  .flyer p, .flyer ul { margin: 0; padding: 0; }
  .decor { position: absolute; left: 0; top: 0; }
  .block { position: absolute; font-size: 10.4px; line-height: 14.1px; }
  .h-main {
    font-family: "Saira Semi Condensed", sans-serif; font-weight: 700;
    color: var(--orange); font-size: 17px; line-height: 18px; margin: 0; letter-spacing: .2px;
  }
  .h-sub {
    font-family: "Saira Semi Condensed", sans-serif; font-weight: 400;
    color: var(--green); font-size: 15px; line-height: 16px; margin: 0;
  }
  .brand {
    position: absolute; left: 28px; top: 66px; width: 140px; text-align: center;
    font-family: "Didact Gothic", sans-serif; font-size: 14px; color: #222; letter-spacing: .3px;
  }
  .brand-dot {
    display: block; width: 38px; height: 38px; margin: 0 auto 8px;
    border-radius: 50%; background: var(--green);
  }
  .check-list { list-style: none; }
  .check-list li { position: relative; padding-left: 17px; }
  .check-list li::before {
    content: "\2714"; position: absolute; left: 0; top: 0; color: var(--orange); font-size: 10px;
  }
  .goal-list { line-height: 12.1px; }
  .goal-list li + li { margin-top: 8.5px; }
  .plus-list { list-style: none; line-height: 12.1px; }
  .plus-list li { position: relative; padding-left: 17px; }
  .plus-list li + li { margin-top: 8.6px; }
  .plus-list li::before {
    content: "+"; position: absolute; left: 0; top: -2px; color: var(--green);
    font-weight: 700; font-size: 14px; font-family: Arial, sans-serif;
  }
  .square-list { list-style: none; display: grid; grid-template-columns: 108px 110px; line-height: 14px; }
  .square-list li { position: relative; padding-left: 10px; }
  .square-list li::before {
    content: ""; position: absolute; left: 0; top: 5px; width: 3px; height: 3px; background: var(--text);
  }
  .format-grid {
    position: absolute; left: 909px; top: 270px; width: 147px; height: 149px;
  }
  .tile {
    position: absolute; width: 72px; height: 73px; border-radius: 5px;
    background: linear-gradient(135deg, var(--orange-light), var(--orange));
    color: var(--white); font-size: 7.4px; line-height: 9.2px; box-sizing: border-box; padding: 5px 6px;
  }
  .tile-tl { left: 0; top: 0; }
  .tile-tr { left: 75px; top: 0; }
  .tile-bl { left: 0; top: 76px; padding-top: 40px; }
  .tile-br { left: 75px; top: 76px; padding-top: 40px; }
  .format-center {
    position: absolute; left: 31px; top: 39px; width: 85px; height: 71px; border-radius: 8px;
    background: var(--white); display: flex; align-items: center; justify-content: center; text-align: center;
    font-family: "Saira Semi Condensed", sans-serif; font-weight: 700; color: var(--orange);
    font-size: 12px; line-height: 14px;
  }
  .photo-portrait, .photo-laptop { position: absolute; border-radius: 50%; box-shadow: 0 0 0 5px var(--ring); }
  .photo-portrait {
    left: 1029px; top: -35px; width: 196px; height: 196px;
    background: linear-gradient(135deg, #dfe4e8, #9aa3a8 55%, #3a4058);
  }
  .photo-laptop {
    left: 404px; top: 470px; width: 218px; height: 218px;
    background: linear-gradient(160deg, #f2f2f2, #8a8f88 45%, #7a9a45 70%, #c7c2b6);
  }
</style>
</head>
<body>
<div class="flyer">

  <svg class="decor" width="1200" height="600" viewBox="0 0 1200 600" aria-hidden="true">
    <path d="M0 0 H1200 V40 C1050 62 850 116 600 118 C400 118 250 100 150 90 L0 60 Z" fill="var(--white)"/>
    <path d="M165 90 C300 108 450 118 600 116 C800 112 950 80 1030 46 L1032 53 C950 90 800 122 600 124 C450 126 300 114 165 96 Z" fill="var(--green-soft)"/>
    <circle cx="90" cy="14" r="117" fill="#e6e6e6"/>
    <circle cx="90" cy="12" r="112" fill="var(--white)"/>
  </svg>

  <div class="brand"><span class="brand-dot"></span>REFLEXION AM UFER</div>

  <div class="photo-portrait" role="img" aria-label="Foto: Beraterin lächelnd am Laptop vor einem Fenster"></div>

  <!-- Spalte 1 -->
  <h2 class="h-main block" style="left:46px;top:158px;">MEINE FACHGEBIETE</h2>
  <h3 class="h-sub block" style="left:46px;top:200px;">SYSTEMISCHE SUPERVISION</h3>
  <p class="block" style="left:46px;top:222px;width:240px;">Bietet Ihnen und Ihrem Team einen geschützten Raum Ihren Arbeitskontext, komplexe Anforderun-gen und Strukturen moderiert zu reflektieren sowie Konflikte, Rollen und Fragestellungen zu klären.</p>
  <p class="block" style="left:46px;top:298px;font-size:12.5px;">Ziele</p>
  <ul class="check-list goal-list block" style="left:46px;top:316px;width:220px;">
    <li>Rollensicherheit und Teamfähigkeit weiterentwickeln</li>
    <li>tiefes Verständnis der beruflichen Situation, Handlungsmöglichkeiten und Perspektiven entwickeln.</li>
    <li>Qualitätssicherung.</li>
    <li>Stärken &amp; Kompetenzen bewusst machen</li>
    <li>langfristig die Freude an Ihrer Arbeit erhalten</li>
  </ul>
  <ul class="square-list block" style="left:63px;top:454px;">
    <li>Einzelsupervision</li><li>Gruppensupervision</li>
    <li>Teamsupervision</li><li>Fallsupervision</li>
  </ul>

  <!-- Spalte 2 -->
  <h3 class="h-sub block" style="left:310px;top:158px;">SYSTEMISCHES COACHING</h3>
  <p class="block" style="left:310px;top:181px;width:245px;">Erweitern Sie Ihre beruflichen Handlungsstrategien und machen Sie Ihre Stärken und Fähigkeiten nutz-bar, um Ihr Ziel zu erreichen. Persönliche Zufriedenheit und professionelle Leistungsfähigkeit stehen im Fokus.</p>
  <h3 class="h-sub block" style="left:310px;top:269px;">LIFECOACHING</h3>
  <p class="block" style="left:310px;top:291px;width:240px;">Im Mittelpunkt stehen Ihre persönlichen Sorgen, Wünsche und Anliegen.<br>Gemeinsam erarbeiten wir Ihr konkretes Ziel und gehen auf Schatzsuche, entdecken neue Perspe-ktiven, Handlungsoptionen, die Sie Schritt für Schritt Ihrem persönlichen Erfolg näherbringen.</p>
  <h3 class="h-sub block" style="left:310px;top:397px;">DIGITALE BERATUNG</h3>
  <p class="block" style="left:310px;top:420px;width:240px;">Endlich können Sie ganz einfach ungenutzte Zeit<br>auf dem Weg zur Arbeit, in Wart-<br>ebereichen oder Zwischen-<br>durch nutzen, um Ihre<br>Ziele und Wünsche<br>wahr werden zu<br>lassen.</p>
  <div class="photo-laptop" role="img" aria-label="Foto: Laptop mit geöffneter Beratungs-Webseite neben gelber Tasse und Pflanze"></div>

  <!-- Spalte 3 -->
  <h2 class="h-main block" style="left:641px;top:158px;">BEI MIR ERHALTEN SIE</h2>
  <ul class="plus-list block" style="left:641px;top:184px;width:232px;">
    <li>Eigenen geschützten Account / eigene App</li>
    <li>24 Stunden / 7 Tage in der Woche Zugang</li>
    <li>Visualisierung Ihrer Erfolge</li>
    <li>Eine Vielzahl an Tools und Fragebögen zur konkreten Umsetzungsbegleitung</li>
    <li>Responsive Design / nutzbar auf dem Smart-phone, Tablet, PC</li>
    <li>Höchstmaß an Flexibilität</li>
    <li>Extrem effizient und dadurch zeit- und geldspa-rend</li>
  </ul>
  <p class="block" style="left:641px;top:363px;width:232px;">Entscheiden Sie selbst, ob Sie die Möglichkeit der digitalen Beratung zusätzlich nutzen wollen oder diese die Sitzungen vor Ort komplett ersetzen soll. Sie möchten auf die klassischen Sitzungen nicht verzichten?</p>
  <p class="block" style="left:641px;top:448px;width:232px;">Nutzen Sie die digitale Begleitung dazwischen und/oder nach dem gesamten Beratungsprozess (Follow-Up). So sichern Sie Ihre Erfolge auch lang-fristig und brauchen vor Herausforderungen und Widerständen im Alltag keine Angst mehr haben.</p>

  <!-- Spalte 4 -->
  <h3 class="h-sub block" style="left:909px;top:158px;">VORZÜGE</h3>
  <ul class="check-list block" style="left:909px;top:181px;line-height:19px;">
    <li>Effizienz,</li><li>Mobilität,</li><li>Flexibilität,</li>
  </ul>
  <ul class="check-list block" style="left:1033px;top:181px;line-height:19px;">
    <li>Nachhaltigkeit,</li><li>Sicherheit,</li><li>großmögliche Anonymität.</li>
  </ul>
  <p class="block" style="left:909px;top:244px;font-size:11px;">&#10140; SPAREN SIE ZEIT UND GELD!</p>

  <div class="format-grid">
    <div class="tile tile-tl">Nachhaltiger Erfolg durch digi-tale Begleitung</div>
    <div class="tile tile-tr">rote Faden des Veränderungspro-zesses sichtbar</div>
    <div class="tile tile-bl">Beste Transfer- und Nachbe-gleitung</div>
    <div class="tile tile-br">Zeit- &amp; Orts-unabhängiges Coaching</div>
    <div class="format-center">MEIN FORMAT<br>FÜR IHREN<br>MEHRWERT!</div>
  </div>

  <h3 class="h-sub block" style="left:909px;top:434px;">MEINE WERTE UND HALTUNG</h3>
  <ul class="check-list block" style="left:909px;top:453px;line-height:16.2px;">
    <li>Wertschätzung, Ressourcenorientierung und Respekt</li>
    <li>Systemisch</li>
    <li>Lösungsorientiert</li>
    <li>Kompetenz und Methodenvielfalt</li>
    <li>Nicht für, sondern mit Ihnen!</li>
    <li>Transparenz und Struktur</li>
    <li>Verschwiegenheit und Vertrauen</li>
  </ul>

</div>
</body>
</html>
```